Inspirational Card with Words of Wisdom to Give to Kids

I run basketball camps and give inspirational messages to elementary schools and high schools (www.pastthebrightline.net).

I would like to create a card that has some inspirational thoughts and words of wisdom on it that I can give away...and that students and athletes will keep in their wallet as a reminder of things I've taught them.

I want it to be clean and classy, while not looking too child-like or business-like, as I'd like to be able to give it out to kids, teenagers, and young adults.

The card will be the size of a regular business card and will be double-sided. I would like to use black, orange, gray, and white as the primary colors, with white or gray likely being the background color.
Updates

You're welcome to leave off the title "Wisdom for Life" if desired and just use "The Triple Crown of Success" on the front of the card.

Thanks.

If you choose to leave off the poem, which you're welcome to do, please make one minor addition to the 5-point creed:

Add the words "God and" to "Honour others in everything you say and do" so it becomes:

"Honour God and others in everything you say and do."

Target Market(s)

Children, Teenagers, and Young Adults

Industry/Entity Type

Business

Requirements
Must have
• All the content, although the poem could be removed if necessary.
Should not have
• Nothing basketball-specific, as I want to be able to give it out to any child or teenager.

```html
<!DOCTYPE html>
<html lang="en">
<head>
<meta charset="utf-8">
<title>The Triple Crown of Success – Wallet Card</title>
<link href="https://fonts.googleapis.com/css2?family=Bebas+Neue&display=swap" rel="stylesheet">
<style>
  :root{
    --orange:#ffa800;
    --orange-deep:#f59300;
    --orange-light:#ffb800;
    --ink:#1c1c1c;
    --slate:#6b6b6b;
    --paper:#ffffff;
    --mist:#e9e9e9;
    --backdrop:#d9d9d9;
    --rule:#8a8a8a;
  }
  *{box-sizing:border-box;margin:0;padding:0}
  html,body{width:1157px;height:1200px;overflow:hidden}
  body{background:var(--backdrop);font-family:"Bebas Neue",Impact,sans-serif;position:relative}

  .card{position:absolute;left:123px;width:910px;height:522px;overflow:hidden;
        box-shadow:0 6px 18px rgba(0,0,0,.25)}
  .card--front{top:60px;background:var(--paper)}
  .card--back{top:618px;background:linear-gradient(90deg,var(--paper),var(--mist))}

  /* front */
  .title{position:absolute;right:46px;top:22px;font-size:60px;line-height:1;color:var(--orange);letter-spacing:.5px}
  .band{position:absolute;left:0;top:80px;width:100%;height:265px;background:var(--orange)}
  .band-edge{position:absolute;left:0;top:345px;width:100%;height:10px;display:block}
  .lower{position:absolute;left:0;top:355px;width:100%;bottom:0;background:linear-gradient(180deg,#f2f2f2,var(--mist))}

  .rule-row{position:absolute;left:45px;display:flex;align-items:center;gap:12px}
  .rule-row--never{top:104px}
  .rule-row--dont{top:185px}
  .rule-row--always{top:265px}
  .tag{display:inline-block;height:56px;line-height:60px;padding:0 30px 0 8px;font-size:56px;color:var(--paper);
       background:linear-gradient(180deg,#4a4a4a,#222);
       clip-path:polygon(0 0,88% 0,100% 50%,88% 100%,0 100%)}
  .rule-row--never .tag{width:152px}
  .rule-row--dont .tag{width:152px}
  .rule-row--always .tag{width:190px}
  .items{font-size:28px;color:var(--ink);letter-spacing:.3px}
  .dot{display:inline-block;width:8px;height:8px;background:var(--ink);transform:rotate(45deg);margin:0 6px 5px}

  .quote{position:absolute;right:46px;top:360px;text-align:right;font-size:25px;line-height:39px;color:var(--ink);letter-spacing:.3px}
  .quote em{font-style:normal;color:var(--orange)}

  /* back */
  .creed{position:absolute;left:0;top:0;width:551px;height:100%;
         background:linear-gradient(90deg,var(--orange-deep),var(--orange-light))}
  .creed-edge{position:absolute;left:551px;top:0;width:12px;height:100%;display:block}
  .creed-title{position:absolute;left:40px;top:24px;font-size:60px;line-height:1;color:var(--paper)}
  .creed-list{position:absolute;left:40px;top:84px;list-style:none;font-size:36px;line-height:40px;color:var(--slate)}
  .num{display:inline-block;background:var(--ink);color:var(--paper);padding:0 3px;margin-right:3px;line-height:36px}

  .pledge{position:absolute;right:46px;top:30px;text-align:right;font-size:31px;line-height:40px}
  .pledge-head{color:var(--ink)}
  .pledge-body{color:var(--orange);margin-top:6px}
  .sign-line{position:absolute;right:46px;width:249px;border-top:2px solid var(--rule)}
  .sign-line--name{top:382px}
  .sign-line--sig{top:461px}
  .sign-label{position:absolute;right:46px;font-size:24px;color:var(--slate)}
  .sign-label--name{top:393px}
  .sign-label--sig{top:472px}
</style>
</head>
<body>

<section class="card card--front" aria-label="Front of card">
  <h1 class="title">The Triple Crown of Success</h1>
  <div class="band"></div>
  <svg class="band-edge" viewBox="0 0 910 10" preserveAspectRatio="none" aria-hidden="true">
    <defs>
      <pattern id="teeth-down" width="16" height="10" patternUnits="userSpaceOnUse">
        <path d="M0 0 L8 10 L16 0Z" fill="#ffa800"/>
      </pattern>
    </defs>
    <rect width="910" height="10" fill="#f2f2f2"/>
    <rect width="910" height="10" fill="url(#teeth-down)"/>
  </svg>
  <div class="lower"></div>

  <div class="rule-row rule-row--never"><span class="tag">Never</span>
    <span class="items">Lie<i class="dot"></i>Cheat<i class="dot"></i>Steal</span></div>
  <div class="rule-row rule-row--dont"><span class="tag">Don’t</span>
    <span class="items">Blame<i class="dot"></i>Complain<i class="dot"></i>Give Up</span></div>
  <div class="rule-row rule-row--always"><span class="tag">Always</span>
    <span class="items">Be Grateful<i class="dot"></i>Uplift Others<i class="dot"></i>Do More Than Your Share</span></div>

  <p class="quote">
    Four things a man must learn to do if he would make his life more <em>true</em>:<br>
    To <em>think</em> without confusion <em>clearly</em>, to <em>love</em> his fellow man <em>sincerely</em>,<br>
    to <em>act</em> from honest motives <em>purely</em>, to <em>trust</em> in God and heaven <em>securely</em>.<br>
    Rev. Harold Vance Dale
  </p>
</section>

<section class="card card--back" aria-label="Back of card">
  <div class="creed"></div>
  <svg class="creed-edge" viewBox="0 0 12 522" preserveAspectRatio="none" aria-hidden="true">
    <defs>
      <pattern id="teeth-side" width="12" height="16" patternUnits="userSpaceOnUse">
        <path d="M0 0 L12 8 L0 16Z" fill="#ffb800"/>
      </pattern>
    </defs>
    <rect width="12" height="522" fill="url(#teeth-side)"/>
  </svg>
  <h2 class="creed-title">A 5-Point Creed</h2>
  <ol class="creed-list">
    <li><span class="num">1.</span>Be intentional to grow and<br>learn new things each day.</li>
    <li><span class="num">2.</span>Honour God and others in everything<br>you say and do.</li>
    <li><span class="num">3.</span>Act with integrity and<br>uprightness in all matters.</li>
    <li><span class="num">4.</span>Prioritize serving and giving<br>to others above yourself.</li>
    <li><span class="num">5.</span>Dream, pray, and expect for<br>the impossible.</li>
  </ol>

  <div class="pledge">
    <p class="pledge-head">Triple Crown &amp;<br>5-Point Creed Pledge:</p>
    <p class="pledge-body">I commit to doing<br>my best to live<br>out the Triple Crown<br>and 5-Point Creed<br>each day.</p>
  </div>
  <div class="sign-line sign-line--name"></div>
  <span class="sign-label sign-label--name">Name</span>
  <div class="sign-line sign-line--sig"></div>
  <span class="sign-label sign-label--sig">Signature</span>
</section>

</body>
</html>
```